Mouthguard Marketing

We specialise in the production of custom made mouthguards for sportsmen and women. These are made by direct public contact or via Dental Surgeons. On our postcard we would need the following...
*Custom made sports guards from £20 (Boxed)
Bleaching trays from £28 (pair) (Boxed)
Orthodontic retainers £28 (pair)
All the above manufactured from advanced pressure and vacuum forming techniques.
Please contact Tom or Gary (01872) 552317 Harlow Dental Laboratory Ltd

Industry/Entity Type

Dental

```html
<!DOCTYPE html>
<html lang="en">
<head>
<meta charset="utf-8">
<title>Mouthguard Postcard</title>
<link href="https://fonts.googleapis.com/css2?family=Kalam:wght@700&family=Roboto+Condensed:wght@400;700&family=Roboto:wght@300;400&display=swap" rel="stylesheet">
<style>
:root{
  --board:#5b9be0;
  --paper:#ffffff;
  --navy:#1f2f8f;
  --royal:#2a3aa0;
  --red:#c8102e;
  --grey:#555a66;
  --rule:#8d97c7;
}
*{margin:0;padding:0;box-sizing:border-box}
html,body{width:807px;height:1200px;overflow:hidden;background:var(--board)}
.canvas{position:relative;width:807px;height:1200px}
.card{position:absolute;left:55px;width:697px;background:var(--paper);overflow:hidden;box-shadow:0 2px 8px rgba(0,0,0,.25)}
.card--front{top:44px;height:540px}
.card--back{top:614px;height:542px}

.member{position:absolute;display:flex;align-items:center;gap:12px;font-family:"Roboto",sans-serif;color:var(--royal)}
.member__mark{width:30px;height:30px;background:var(--royal)}
.member__name{font-weight:300;font-size:12px;line-height:1.3}
.member__status{font-weight:300;font-size:21px;line-height:1.2}
.card--front .member{left:27px;top:28px}
.card--back .member{left:350px;top:28px}
.card--back .member__mark{width:22px;height:22px}
.card--back .member__name{font-size:9px}
.card--back .member__status{font-size:15px}

.product-photo{position:absolute;left:442px;top:0;width:255px;height:190px;border-radius:0 0 0 60% / 0 0 0 40%;background:linear-gradient(160deg,#c8263a 0%,#f3f3f7 35%,#2c47b8 55%,#1b2f9a 100%)}

.headline{position:absolute;left:27px;top:138px;font-family:"Kalam",cursive;font-weight:700;font-style:italic;font-size:45px;line-height:1;color:var(--red);transform:rotate(-3deg);transform-origin:left bottom;white-space:nowrap}
.subline{position:absolute;left:104px;top:196px;font-family:"Kalam",cursive;font-weight:700;font-style:italic;font-size:20px;line-height:25px;color:var(--navy);transform:rotate(-3deg);transform-origin:left top;white-space:nowrap}

.price-list{position:absolute;left:27px;top:287px;list-style:none;font-family:"Roboto Condensed",sans-serif;font-size:16px;line-height:24px;color:var(--navy)}
.price-list li{display:flex;align-items:center;gap:6px}
.price-list svg{width:18px;height:20px;flex:none}

.contact{position:absolute;font-family:"Roboto Condensed",sans-serif;color:var(--navy)}
.contact__lead{font-size:14.5px;margin-bottom:8px}
.contact__name{font-weight:700;font-size:16px;line-height:20px;color:var(--red);white-space:nowrap}
.card--front .contact{left:476px;top:302px}
.card--back .contact{left:22px;top:372px}
.card--back .contact__lead{font-size:14px}
.card--back .contact__name{font-size:14.5px;line-height:18px}

.swoosh{position:absolute;left:0;top:380px;width:697px;height:160px}
.sport-photo{position:absolute;top:395px;width:153px;height:109px;box-shadow:0 2px 5px rgba(0,0,0,.35)}
.sport-photo--football{left:51px;background:linear-gradient(180deg,#4b5a3a 0%,#7e9a3e 45%,#5c8a2c 100%)}
.sport-photo--boxing{left:219px;background:linear-gradient(180deg,#7a4a2a 0%,#c58a3d 50%,#d9a455 100%)}

.partner{position:absolute;left:485px;top:455px;display:flex;align-items:center;gap:8px;font-family:"Roboto Condensed",sans-serif;font-size:19px;color:var(--grey)}
.partner__mark{width:14px;height:14px;border-radius:50%;background:var(--royal)}

.choose{position:absolute;left:22px;width:200px;font-family:"Kalam",cursive;font-weight:700;font-style:italic;font-size:15px;line-height:18px;transform:rotate(-3deg);transform-origin:left top;white-space:nowrap}
.choose span{display:block}
.choose__lead{color:var(--navy)}
.choose__count{color:var(--red)}
.choose--colours{top:34px}
.choose--glitter{top:84px}

.about{position:absolute;left:22px;top:148px;width:186px;font-family:"Roboto Condensed",sans-serif;font-size:14px;line-height:19px;color:var(--navy)}

.swatches{position:absolute;left:236px;top:20px;list-style:none}
.swatches li{height:37.8px}
.swatch{display:block;margin-left:22px;width:56px;height:18px;border-radius:3px 10px 10px 3px}
.swatch__label{display:block;font-family:"Roboto Condensed",sans-serif;font-weight:700;font-size:7px;color:var(--navy);margin-top:6px;white-space:nowrap}
.swatch--yellow-green{background:linear-gradient(90deg,#c9e33b,#e3d52f)}
.swatch--maroon-green{background:linear-gradient(90deg,#8a2a2a 0 60%,#7ac143 60%)}
.swatch--union{background:linear-gradient(90deg,#b8203a,#2a3a9a)}
.swatch--st-george{background:linear-gradient(90deg,#f0f0f0 0 40%,#c8102e 40% 55%,#e8e8e8 55%)}
.swatch--goofy{background:linear-gradient(90deg,#555 0 30%,#eee 30% 60%,#555 60%)}
.swatch--fangs{background:linear-gradient(90deg,#222,#555)}
.swatch--stars{background:linear-gradient(90deg,#2a3a8a 0 45%,#c8102e 45%)}
.swatch--chequered{background:linear-gradient(90deg,#2e8a3a,#c7e3b0)}
.swatch--purple{background:linear-gradient(90deg,#4b2a8a,#7a4ab8)}
.swatch--pink{background:linear-gradient(90deg,#c2146e,#e84ca0)}
.swatch--gold{background:linear-gradient(90deg,#d9a520,#f0c843)}

.divider{position:absolute;left:336px;top:24px;width:1px;height:424px;background:var(--rule)}
</style>
</head>
<body>
<main class="canvas">

  <section class="card card--front">
    <div class="member">
      <span class="member__mark"></span>
      <div>
        <div class="member__name">Dental Workshops Federation</div>
        <div class="member__status">Registered Member</div>
      </div>
    </div>

    <div class="product-photo" role="img" aria-label="Custom mouthguard with a red, white and blue flag design"></div>

    <h1 class="headline">Guard your mouth</h1>
    <p class="subline">with custom made mouthguards<br>for sportsmen and women.</p>

    <ul class="price-list">
      <li><svg viewBox="0 0 18 20"><path d="M2 11 L7 17 L16 2" fill="none" stroke="#c8102e" stroke-width="2.4" stroke-linecap="round" stroke-linejoin="round"/></svg>Custom made sports guards from £20 (Boxed)</li>
      <li><svg viewBox="0 0 18 20"><path d="M2 11 L7 17 L16 2" fill="none" stroke="#c8102e" stroke-width="2.4" stroke-linecap="round" stroke-linejoin="round"/></svg>Bleaching trays from £28 (pair) (Boxed)</li>
      <li><svg viewBox="0 0 18 20"><path d="M2 11 L7 17 L16 2" fill="none" stroke="#c8102e" stroke-width="2.4" stroke-linecap="round" stroke-linejoin="round"/></svg>Orthodontic retainers £28 (pair)</li>
    </ul>

    <div class="contact">
      <p class="contact__lead">For questions, please contact</p>
      <p class="contact__name">Tom or Gary (01872) 552317</p>
      <p class="contact__name">Harlow Dental Laboratory Ltd</p>
    </div>

    <svg class="swoosh" viewBox="0 0 697 160" preserveAspectRatio="none" aria-hidden="true">
      <path d="M0 60 C150 10 330 40 450 160 L0 160 Z" fill="#2a3aa0"/>
    </svg>

    <div class="sport-photo sport-photo--football" role="img" aria-label="Football players contesting the ball on grass"></div>
    <div class="sport-photo sport-photo--boxing" role="img" aria-label="Boxing gloves resting on a gym floor"></div>

    <div class="partner">
      <span class="partner__mark"></span>
      <span>Northgate Dental Craft</span>
    </div>
  </section>

  <section class="card card--back">
    <p class="choose choose--colours"><span class="choose__lead">Choose from</span><span class="choose__count">26 vibrant colours!</span></p>
    <p class="choose choose--glitter"><span class="choose__lead">Choose from</span><span class="choose__count">6 different glitter designs!</span></p>

    <p class="about">We specialise in the production of custom made mouthguards for sportsmen and women. Our mouthguards are available in a range of standard colours, giving you the option to choose your favorite colour or team colours. Each is made by direct public contact or via Dental Surgeons using advanced pressure and vacuum forming techniques.</p>

    <div class="contact">
      <p class="contact__lead">For questions, please contact</p>
      <p class="contact__name">Tom or Gary (01872) 552317</p>
      <p class="contact__name">Harlow Dental Laboratory Ltd</p>
    </div>

    <ul class="swatches">
      <li><span class="swatch swatch--yellow-green" role="img" aria-label="Mouthguard sample, two stripes"></span><span class="swatch__label">2 Stripes (MC2)</span></li>
      <li><span class="swatch swatch--maroon-green" role="img" aria-label="Mouthguard sample, seven stripes"></span><span class="swatch__label">7 Stripes (MC7)</span></li>
      <li><span class="swatch swatch--union" role="img" aria-label="Mouthguard sample, union flag design"></span><span class="swatch__label">SD Union Jack</span></li>
      <li><span class="swatch swatch--st-george" role="img" aria-label="Mouthguard sample, St George cross design"></span><span class="swatch__label">SD St George</span></li>
      <li><span class="swatch swatch--goofy" role="img" aria-label="Mouthguard sample, goofy teeth design"></span><span class="swatch__label">SD Goofy</span></li>
      <li><span class="swatch swatch--fangs" role="img" aria-label="Mouthguard sample, fangs design"></span><span class="swatch__label">SD Fangs</span></li>
      <li><span class="swatch swatch--stars" role="img" aria-label="Mouthguard sample, stars and stripes design"></span><span class="swatch__label">SD Stars and Stripes</span></li>
      <li><span class="swatch swatch--chequered" role="img" aria-label="Mouthguard sample, chequered design"></span><span class="swatch__label">SD Chequered Example</span></li>
      <li><span class="swatch swatch--purple" role="img" aria-label="Mouthguard sample, purple glitter"></span><span class="swatch__label">Purple Glitter</span></li>
      <li><span class="swatch swatch--pink" role="img" aria-label="Mouthguard sample, pink glitter"></span><span class="swatch__label">Pink Glitter</span></li>
      <li><span class="swatch swatch--gold" role="img" aria-label="Mouthguard sample, yellow glitter"></span><span class="swatch__label">Yellow Glitter</span></li>
    </ul>

    <div class="divider"></div>

    <div class="member">
      <span class="member__mark"></span>
      <div>
        <div class="member__name">Dental Workshops Federation</div>
        <div class="member__status">Registered Member</div>
      </div>
    </div>
  </section>

</main>
</body>
</html>
```